Energy Company 8-page Brochure

We are in need of a redesign of our 8-page brochure. Attached is the initial design that does not represent us very well. We are looking for CLEAN/CORPORATE look with a little bit of flair (graphs/charts if applicable).

I prefer white background and our company colors (blue/green) to be the accent colors. Feel free to add additional accent colors to highlight certain areas.

We are in the energy field (not just solar), so please consider the types of images that you will use. Are headquarters is located in Chicago, IL so a great looking picture of the skyline or something similar would work for the front and back cover.

We have additional marketing collateral that we will want to be uniformed once we have the right design.

Good luck, and we look forward to receiving some great designs!

Best Regards,
Kurt

Target Market(s)

Small to large businesses (B2B).

Industry/Entity Type

It Company

Colors
ffffff
9bcb3c
0255a3

Requirements
Must have
• Clean design, company colors, specified content and editable files.
Nice to have
• Graphs, charts, highlighted areas where necessary.
Should not have
• Clutter! Please utilized page space appropriately. There is a lot of content, so you need to consider graphics and image placement.

```html
<!DOCTYPE html>
<html lang="en">
<head>
<meta charset="utf-8">
<title>Brightwell Energy – Brochure Front Cover</title>
<link rel="stylesheet" href="https://fonts.googleapis.com/css2?family=Jost:wght@400;500;700;800&display=swap">
<style>
  :root {
    --stage: #e4e5e7;
    --paper: #ffffff;
    --brand-blue: #0255a3;
    --brand-green: #9bcb3c;
    --accent-orange: #e0832a;
    --night-deep: #1f2f6e;
    --night-glow: #c9822e;
    --slate: #3b4a57;
    --slate-dark: #2a3640;
    --text-light: #ffffff;
  }
  * { margin: 0; padding: 0; box-sizing: border-box; }
  html, body {
    width: 1200px; height: 1000px; overflow: hidden;
    background: var(--stage);
    font-family: "Jost", "Futura", sans-serif;
  }
  .stage {
    position: relative; width: 1200px; height: 1000px;
    display: flex; align-items: center; justify-content: center;
  }
  .cover {
    position: relative; width: 640px; height: 900px;
    background: var(--paper);
    box-shadow: 0 10px 30px rgba(0,0,0,0.18);
    overflow: hidden;
  }
  .cover-header {
    height: 150px; display: flex; align-items: center; padding-left: 44px;
  }
  .brand { display: flex; align-items: center; gap: 14px; }
  .brand-dot {
    width: 44px; height: 44px; border-radius: 50%;
    background: var(--brand-blue);
  }
  .brand-name {
    font-size: 30px; font-weight: 500; color: var(--brand-blue); line-height: 1;
  }
  .accent-rule { height: 6px; background: var(--brand-green); }
  .hero {
    position: relative; height: 390px;
    background:
      radial-gradient(ellipse at 55% 85%, rgba(240,170,70,0.75), transparent 60%),
      radial-gradient(ellipse at 20% 70%, rgba(220,140,60,0.5), transparent 55%),
      linear-gradient(180deg, var(--night-deep) 0%, #3a4a8a 30%, #6a5a6a 60%, var(--night-glow) 100%);
  }
  .hero-title {
    position: absolute; left: 40px; right: 40px; bottom: 44px; color: var(--text-light);
    line-height: 0.92;
  }
  .hero-kicker { font-size: 46px; font-weight: 500; letter-spacing: 1px; }
  .hero-word { font-size: 122px; font-weight: 800; letter-spacing: -2px; white-space: nowrap; }
  .value-band {
    position: relative; height: 120px; background: var(--accent-orange);
    display: flex; align-items: flex-end; justify-content: space-between;
    padding: 0 40px 18px;
  }
  .value-statement {
    color: var(--text-light); font-size: 15px; font-weight: 500;
    letter-spacing: 0.8px; text-transform: uppercase; line-height: 1.35;
  }
  .partner-badge {
    align-self: center; width: 130px; height: 52px; border-radius: 6px;
    background: #f3f7ea;
  }
  .services {
    position: relative; height: 234px;
    background: linear-gradient(180deg, var(--slate) 0%, var(--slate-dark) 100%);
    color: var(--text-light);
  }
  .service-list {
    position: absolute; right: 40px; top: 26px; list-style: none;
    font-size: 19px; font-weight: 400; line-height: 1.5;
  }
  .cover-footer {
    position: absolute; left: 40px; bottom: 28px;
    display: flex; align-items: center; gap: 10px;
  }
  .cover-footer .brand-dot {
    width: 22px; height: 22px; background: var(--text-light);
  }
  .cover-footer .brand-name { font-size: 20px; color: var(--text-light); font-weight: 500; }
</style>
</head>
<body>
  <main class="stage">
    <article class="cover">
      <header class="cover-header">
        <div class="brand">
          <span class="brand-dot"></span>
          <span class="brand-name">Brightwell Energy</span>
        </div>
      </header>
      <div class="accent-rule"></div>
      <section class="hero" role="img" aria-label="Aerial photograph of a city skyline at night with glowing streets">
        <h1 class="hero-title">
          <span class="hero-kicker">EVERYTHING</span><br>
          <span class="hero-word">ENERGY</span>
        </h1>
      </section>
      <section class="value-band">
        <p class="value-statement">We are dedicated to helping you<br>lower your company's operating costs.</p>
        <div class="partner-badge" aria-hidden="true"></div>
      </section>
      <section class="services" role="img" aria-label="Photograph of electrical transmission towers in a dark blue-grey tone">
        <ul class="service-list">
          <li>We manage pricing volatility.</li>
          <li>We mitigate risk.</li>
          <li>We secure the lowest cost.</li>
          <li>We lower energy usage.</li>
          <li>We reflect your energy values.</li>
        </ul>
        <div class="cover-footer">
          <span class="brand-dot"></span>
          <span class="brand-name">Brightwell Energy</span>
        </div>
      </section>
    </article>
  </main>
</body>
</html>
```